Wordpress Website for electrician

I'm looking for an easy to maintain website for my electrical contracting business. Need a professional and appealing site.
Im wanting a website where clients can come on and look at services we offer, case studies and advertise our services.
Colours I'm wanting to incorporate are green, white, black and grey
I'm wanting a big slide show on main page where I can place advertising etc.
Menu is to include home, services, our work, specials, energy efficiency and contact
My existing site is www.brivolelectric.com.au
looking for something with a similar layout to this website
Target Market(s)
Businesses
Industry/Entity Type
Electrician
Look and feel

```html
<!DOCTYPE html>
<html lang="en">
<head>
<meta charset="utf-8">
<title>Brivol Electric – Electrical Contractor</title>
<link rel="stylesheet" href="https://fonts.googleapis.com/css2?family=Questrial&family=Dosis:wght@700;800&family=Roboto:wght@400;500&display=swap">
<style>
:root{
  --green:#3db54a;
  --green-dark:#2f9a3b;
  --ink:#231f20;
  --grey:#808080;
  --text:#8a8a8a;
  --footer:#2b2828;
  --footer-bottom:#0d0d0d;
  --white:#ffffff;
}
*{box-sizing:border-box;margin:0;padding:0}
html,body{width:1200px;height:932px;overflow:hidden}
body{position:relative;background:var(--white);font-family:"Roboto",Arial,sans-serif;color:var(--text)}
.abs{position:absolute}
a{color:inherit;text-decoration:none}

/* header */
.site-header{left:0;top:0;width:1200px;height:86px;background:linear-gradient(#ffffff,#e9e9e9)}
.brand{left:200px;top:22px;display:flex;align-items:center;gap:8px;font-family:"Questrial",sans-serif;font-size:26px;color:var(--green)}
.brand-dot{width:18px;height:18px;border-radius:50%;background:var(--ink)}
.search{left:808px;top:8px;width:193px;height:24px;border:1px solid #cfcfcf;background:#fff;font-size:10px;color:#999;padding:5px 6px;font-family:"Questrial",sans-serif}
.search svg{position:absolute;right:6px;top:3px}
.phone{right:199px;top:34px;display:flex;align-items:center;gap:6px;font-family:"Questrial",sans-serif;font-size:27px;color:var(--ink)}

/* nav */
.main-nav{left:0;top:86px;width:1200px;height:38px;background:var(--ink)}
.main-nav ul{position:absolute;left:199px;top:0;display:flex;list-style:none;height:38px}
.main-nav li{font-family:"Questrial",sans-serif;font-size:14px;color:#fff;line-height:38px;padding:0 12px;border-right:1px solid #555}
.main-nav li:first-child{padding-left:0}
.main-nav li:last-child{border-right:none}
.social{right:199px;top:95px;display:flex;gap:6px}
.social span{width:20px;height:20px;border-radius:50%;background:#8c8c8c}

/* hero */
.hero{left:0;top:124px;width:1200px;height:285px;background:var(--green)}
.hero-title{left:199px;top:153px;font-family:"Dosis",sans-serif;font-weight:800;font-size:36px;line-height:1;color:#fff;letter-spacing:.3px}
.hero-text{left:200px;top:205px;width:380px;font-size:9.3px;line-height:14.4px;color:#fff}
.btn-dark{height:36px;width:120px;background:var(--ink);color:#fff;font-size:12px;font-weight:500;display:flex;align-items:center;justify-content:center;border:1px solid #111;box-shadow:inset 0 0 0 1px #444}

.slide{left:662px;top:150px;width:339px;height:232px;border-radius:8px;background:linear-gradient(#ffffff 0%,#f4f8f2 60%,#cfe6c6 100%);overflow:hidden}
.slide-line1{left:662px;top:240px;width:339px;text-align:center;font-family:"Dosis",sans-serif;font-weight:800;font-size:40px;color:var(--green);line-height:1}
.slide-line2{left:662px;top:280px;width:339px;text-align:center;font-family:"Dosis",sans-serif;font-weight:800;font-size:30px;color:#000;line-height:1}
.dots{left:676px;top:363px;display:flex;gap:3px}
.dots span{width:8px;height:8px;border-radius:50%;background:#999}
.dots span.on{background:#1e8f8f}
.arrows{left:944px;top:358px;display:flex;gap:6px}
.arrows span{width:20px;height:20px;border-radius:50%;background:#fff;border:1px solid #bbb;display:flex;align-items:center;justify-content:center}

/* welcome */
.welcome{left:200px;top:452px;font-family:"Questrial",sans-serif;font-weight:400;font-size:30px;color:var(--grey)}
.welcome b{font-weight:400;color:var(--green)}
.intro{left:199px;top:490px;width:515px;font-size:9.6px;line-height:14.4px;letter-spacing:.1px}
.btn-green{background:var(--green);color:#fff;font-size:11px;display:flex;align-items:center;justify-content:center;border:1px solid var(--green-dark)}
.divider{left:199px;top:614px;width:511px;height:1px;background:#cfcfcf}

.service{top:639px;width:166px;height:118px;text-align:center}
.service h3{height:43px;font-family:"Questrial",sans-serif;font-weight:400;font-size:17px;line-height:15px;color:#fff;padding-top:8px;border-bottom:1px solid rgba(255,255,255,.25)}
.service p{font-size:9.6px;line-height:13px;color:#fff;padding:13px 6px 0}
.service.green{background:var(--green)}
.service.dark{background:var(--ink)}
.service .more{position:absolute;left:46px;top:97px;width:74px;height:26px;font-size:10px;display:flex;align-items:center;justify-content:center;color:#fff}
.service.green .more{background:var(--ink)}
.service.dark .more{background:var(--green)}

/* sidebar */
.panel{left:738px;width:263px;border:1px solid #cfcfcf;background:#fff}
.panel h2{font-family:"Questrial",sans-serif;font-weight:700;font-size:28px;line-height:33px;color:#fff;padding-left:7px;height:33px}
.news{top:458px;height:166px}
.news h2{background:var(--ink)}
.news-item{position:absolute;left:7px;width:250px;height:37px}
.news-date{position:absolute;left:0;top:-4px;width:38px;text-align:center;font-family:"Questrial",sans-serif;font-size:26px;color:var(--ink);line-height:26px}
.news-date small{display:block;font-size:12px;color:var(--green);line-height:12px}
.news-body{position:absolute;left:44px;top:0;width:206px;height:37px;background:#f1f1f1;font-size:9px;line-height:11.5px;padding:5px 6px;color:#999}
.news-body a{color:var(--green)}
.view-more{position:absolute;left:11px;top:142px;font-size:12px;color:var(--ink);text-decoration:underline}
.testimonials{top:639px;height:124px}
.testimonials h2{background:var(--green)}
.quote-title{position:absolute;left:11px;top:46px;font-size:14px;color:var(--green);font-family:"Questrial",sans-serif}
.quote{position:absolute;left:32px;top:65px;width:220px;font-size:9px;line-height:12px;color:#888}
.quote-mark{position:absolute;left:11px;top:60px;font-size:28px;color:#ccc;font-family:Georgia,serif}
.author{position:absolute;left:11px;top:99px;font-size:12px;color:var(--ink)}

/* footer */
.site-footer{left:0;top:788px;width:1200px;height:105px;background:var(--footer)}
.footer-bottom{left:0;top:893px;width:1200px;height:39px;background:var(--footer-bottom);font-size:9.5px;color:#aaa;text-align:center;line-height:39px}
.f-head{top:795px;font-family:"Questrial",sans-serif;font-size:14px;color:#fff}
.f-links{top:826px;font-size:9.8px;line-height:17.6px;color:#aaa;list-style:none}
.newsletter{left:486px;top:826px;width:227px;height:30px;background:#fff;border:1px solid #ccc}
.newsletter span{position:absolute;left:7px;top:9px;font-size:9.5px;color:#999}
.subscribe{position:absolute;right:2px;top:2px;width:82px;height:24px;background:var(--green);color:var(--ink);font-family:"Questrial",sans-serif;font-weight:700;font-size:13px;display:flex;align-items:center;justify-content:center;border:1px solid var(--green-dark)}
.f-email{right:199px;top:826px;font-size:9.8px;color:#aaa}
.f-phone{right:199px;top:840px;font-family:"Questrial",sans-serif;font-size:23px;color:#8a8a8a}
</style>
</head>
<body>

<header class="abs site-header">
  <div class="abs brand"><span class="brand-dot"></span>Brivol Electric</div>
  <div class="abs search">Search
    <svg width="18" height="18" viewBox="0 0 18 18"><circle cx="7" cy="7" r="5" fill="none" stroke="#3db54a" stroke-width="2"/><line x1="11" y1="11" x2="16" y2="16" stroke="#3db54a" stroke-width="2.5" stroke-linecap="round"/></svg>
  </div>
  <div class="abs phone">
    <svg width="24" height="22" viewBox="0 0 24 24"><path d="M6.6 10.8a15 15 0 0 0 6.6 6.6l2.2-2.2c.3-.3.7-.4 1-.2 1.1.4 2.3.6 3.6.6.6 0 1 .4 1 1V20c0 .6-.4 1-1 1A17 17 0 0 1 3 4c0-.6.4-1 1-1h3.5c.6 0 1 .4 1 1 0 1.2.2 2.4.6 3.6.1.3 0 .7-.2 1z" fill="#3db54a"/></svg>
    0400-555-018
  </div>
</header>

<nav class="abs main-nav">
  <ul>
    <li>Home</li><li>Services</li><li>Our Work</li><li>Specials</li><li>Energy Efficiency</li><li>Contact</li>
  </ul>
</nav>
<div class="abs social" aria-label="Social links"><span></span><span></span><span></span><span></span></div>

<section class="abs hero"></section>
<h1 class="abs hero-title">LED IS THE FUTURE</h1>
<p class="abs hero-text">LED lighting has involved rapidly in the last 5 years. In the coming years we will see all lighting being substitued with LED lights. It is by far the most efficient form of lighting on todays market. Let us retrofit your business or home with LED and the savings will literally pay the lights off.</p>
<a class="abs btn-dark" style="left:199px;top:300px">WHY LED?</a>
<a class="abs btn-dark" style="left:335px;top:300px">REQUEST QUOTE</a>

<div class="abs slide" role="img" aria-label="Slideshow image: computer monitor showing a light bulb with a tree inside above green grass, with a mouse beside it"></div>
<div class="abs slide-line1">BE GREEN</div>
<div class="abs slide-line2">SAVE MONEY</div>
<div class="abs dots"><span></span><span class="on"></span><span></span><span></span></div>
<div class="abs arrows">
  <span><svg width="8" height="8" viewBox="0 0 8 8"><path d="M6 0L1 4l5 4z" fill="#333"/></svg></span>
  <span><svg width="8" height="8" viewBox="0 0 8 8"><path d="M2 0l5 4-5 4z" fill="#333"/></svg></span>
</div>

<h2 class="abs welcome">Welcome to <b>Brivol Electric</b></h2>
<p class="abs intro">Lorem ipsum dolor sit amet, consectetur adipiscing elit. Quisque gravida risus ligula, ut mollis neque tempor eu. Mauris tempus viverra augue et pretium. Integer non dui quis metus volutpat dictum at nec dui. Fusce eleifend elit sed volutpat euismod. Donec nisl enim, semper id odio eget, suscipit sodales diam. Ut elit eros, semper posuere interdu faucibus, rhoncus ut tellus. Vivamus ante magna,</p>
<a class="abs btn-green" style="left:200px;top:562px;width:79px;height:28px">Read More</a>
<div class="abs divider"></div>

<article class="abs service green" style="left:200px">
  <h3>Electrical<br>Contracting</h3>
  <p>We offer all types of electrical work from Installation to maintenance</p>
  <a class="more">View More</a>
</article>
<article class="abs service dark" style="left:372px">
  <h3>Energy<br>Efficiency</h3>
  <p>With one of our audits to your business or home we can lower</p>
  <a class="more">View More</a>
</article>
<article class="abs service green" style="left:544px">
  <h3>Underground<br>Location</h3>
  <p>We have the tools and knowledge in locating underground utilities.</p>
  <a class="more">View More</a>
</article>

<aside class="abs panel news">
  <h2>News</h2>
  <div class="news-item" style="top:45px">
    <div class="news-date">03<small>Aug</small></div>
    <div class="news-body">Lorem ipsum dolor sit amet, consectetur adipiscing elit. Quisque gravida. <a>Read More...</a></div>
  </div>
  <div class="news-item" style="top:94px">
    <div class="news-date">02<small>Aug</small></div>
    <div class="news-body">Lorem ipsum dolor sit amet, consectetur adipiscing elit. Quisque gravida. <a>Read More...</a></div>
  </div>
  <a class="view-more">View More</a>
</aside>

<aside class="abs panel testimonials">
  <h2>Testimonials</h2>
  <div class="quote-title">Lorem ipsum dolor sit amet.</div>
  <div class="quote-mark">&ldquo;</div>
  <p class="quote">Morbi tincidunt ipsum id enim vehicula lobortis. feugiat eget augue eget dictum. &rdquo;</p>
  <div class="author">Dana Whitcombe</div>
</aside>

<footer class="abs site-footer"></footer>
<div class="abs f-head" style="left:200px">Navigation</div>
<ul class="abs f-links" style="left:199px"><li>Home</li><li>Services</li><li>Our Work</li></ul>
<ul class="abs f-links" style="left:277px"><li>Specials</li><li>Energy Efficiency</li><li>Contact Us</li></ul>
<div class="abs f-head" style="left:486px">Newsletter SignUp</div>
<div class="abs newsletter"><span>Email address...</span><a class="subscribe">Subscribe</a></div>
<div class="abs f-head" style="left:861px">Contact Us</div>
<div class="abs f-email">sales@brivolelectric.com.au</div>
<div class="abs f-phone">0400-555-018</div>
<div class="abs footer-bottom">Brivol Electric is a Registered Eleectrical Contractor - REC. 48152</div>

</body>
</html>
```